Wow me with your Earring card options!

An A7 portrait sized earring card is required for Marble & Mango. Inspired by Marble and fueled by Mango we love our accessories to do the talking. Bold statement earrings are our thing. Our earring cards need to showcase our brand while not stealing all of the limelight from the earrings themselves. Earring care information needs to be included on the back side of the card. Our simple logo needs to be the basis for the colour choices used on the card.

Requirements
Should not have
• No florals please 😊

```html
<!DOCTYPE html>
<html lang="en">
<head>
<meta charset="utf-8">
<title>Marble &amp; Mango – Earring Card</title>
<link rel="stylesheet" href="https://fonts.googleapis.com/css2?family=Great+Vibes&family=Open+Sans:wght@400;600&display=swap">
<style>
  :root {
    --brand-pink: #ec1f7a;
    --brand-orange: #f05a28;
    --logo-black: #0a0b0b;
    --paper: #ffffff;
    --logo-name: #ffffff;
  }
  * { box-sizing: border-box; margin: 0; padding: 0; }
  html, body { width: 1200px; height: 1200px; overflow: hidden; background: var(--paper); }
  .canvas { position: relative; width: 1200px; height: 1200px; font-family: "Open Sans", Arial, sans-serif; }

  .logo-box {
    position: absolute;
    background: var(--logo-black);
    border: solid var(--brand-pink);
    display: flex; align-items: center; justify-content: center;
  }
  .logo-name { color: var(--logo-name); font-weight: 600; white-space: nowrap; }

  .logo-sample { left: 462px; top: 129px; width: 265px; height: 143px; border-width: 9px; }
  .logo-sample .logo-name { font-size: 26px; }

  .card-spread { position: absolute; left: 79px; top: 361px; width: 1044px; height: 708px; background: var(--brand-pink); }
  .card-face { position: absolute; background: var(--paper); }
  .card-front { left: 28px; top: 16px; width: 479px; height: 676px; }
  .card-back { left: 537px; top: 15px; width: 481px; height: 678px; }

  .earring-pattern {
    position: absolute; left: 38px; top: 37px; width: 404px; height: 606px;
    border: 4px solid var(--brand-pink);
    background: linear-gradient(135deg, #fdeef5 0%, #fbfbe6 35%, #eef8e6 65%, #fdf0e8 100%);
  }
  .logo-front { left: 76px; top: 168px; width: 250px; height: 251px; border-width: 9px; }
  .logo-front .logo-name { font-size: 26px; }

  .care-frame { position: absolute; left: 29px; top: 24px; width: 426px; height: 632px; border: 3px solid var(--brand-orange); }
  .logo-back { left: 119px; top: 23px; width: 177px; height: 176px; border-width: 6px; }
  .logo-back .logo-name { font-size: 18px; }

  .care-title {
    position: absolute; left: 0; right: 0; top: 209px; text-align: center;
    font-family: "Great Vibes", cursive; font-weight: 400; font-size: 40px; color: var(--brand-orange); line-height: 1;
  }
  .care-list { position: absolute; left: 39px; top: 265px; list-style: none; color: var(--brand-pink); font-size: 16.5px; }
  .care-list li { height: 27.5px; line-height: 27.5px; }
  .care-list li:last-child { margin-top: 3px; }
  .care-list li::before { content: "•"; margin-right: 7px; }

  .follow-heading, .contact-heading {
    position: absolute; left: 0; right: 0; text-align: center; color: var(--brand-orange); font-size: 19px; line-height: 1;
  }
  .follow-heading { top: 402px; }
  .social-icons { position: absolute; left: 0; right: 0; top: 431px; display: flex; justify-content: center; gap: 6.5px; }
  .social-icons span { width: 29px; height: 29px; border: 1.5px solid var(--brand-orange); border-radius: 50%; }
  .social-handle { position: absolute; left: 0; right: 0; top: 464px; text-align: center; color: var(--brand-orange); font-size: 16px; line-height: 1; }
  .contact-heading { top: 516px; }
  .contact-lines { position: absolute; left: 0; right: 0; top: 540px; text-align: center; color: var(--brand-pink); font-size: 16.5px; line-height: 22px; }
</style>
</head>
<body>
<div class="canvas">
  <div class="logo-box logo-sample"><span class="logo-name">Marble &amp; Mango</span></div>

  <div class="card-spread">
    <section class="card-face card-front">
      <div class="earring-pattern" role="img" aria-label="Scattered pattern of colourful statement earring illustrations in pink, lime, green, teal and orange"></div>
      <div class="logo-box logo-front"><span class="logo-name">Marble &amp; Mango</span></div>
    </section>

    <section class="card-face card-back">
      <div class="care-frame">
        <div class="logo-box logo-back"><span class="logo-name">Marble &amp; Mango</span></div>
        <h2 class="care-title">Earrings Care Instructions</h2>
        <ul class="care-list">
          <li>Avoid moisture &amp; remove before bathing.</li>
          <li>For comforts sake, remove before bed !</li>
          <li>Avoid contact with perfumes &amp; lotions</li>
          <li>Score away from dierct sunlight.</li>
        </ul>
        <p class="follow-heading">Follow us:</p>
        <div class="social-icons"><span></span><span></span><span></span><span></span></div>
        <p class="social-handle">@marbleandmango</p>
        <p class="contact-heading">Contact Us :</p>
        <p class="contact-lines">www.marbleandmango.com.au<br>hello@marbleandmango.com.au</p>
      </div>
    </section>
  </div>
</div>
</body>
</html>
```